Business Card Design - Law Firm

We are a boutique law firm located near the beach in Manly, Australia. We have recently had a new logo designed and are revamping our business cards with the new logo.

We have recently had a business card design done for us but are not entirely happy with it. We are looking for something modern, simplistic but striking. We would like to see multiple designs.

We have attached a word document which includes our new logo and the current business card design which we are looking at moving away from.

We would like the business cards to be double sided. We would like the design to include something which we can print in gloss colour when we send it to the business card printers.

```html
<!DOCTYPE html>
<html lang="en">
<head>
<meta charset="utf-8">
<title>Halden &amp; Partners – Business Card</title>
<link rel="stylesheet" href="https://fonts.googleapis.com/css2?family=Poppins:wght@400;500&display=swap">
<style>
  :root {
    --page-bg: #dedede;
    --card-front: #ffffff;
    --card-back: #2e2e2e;
    --navy: #3b4a9a;
    --periwinkle: #8a9bd6;
    --gold: #b9a06a;
    --ink: #333333;
    --white: #ffffff;
  }
  * { margin: 0; padding: 0; box-sizing: border-box; }
  html, body {
    width: 1200px; height: 1200px; overflow: hidden;
    background: var(--page-bg);
    font-family: "Poppins", sans-serif;
  }
  .card {
    position: absolute; left: 200px;
    width: 800px; height: 457px;
  }
  .card-front { top: 80px; background: var(--card-front); }
  .card-back {
    top: 663px;
    background: linear-gradient(180deg, #353535 0%, var(--card-back) 100%);
  }

  .holder { position: absolute; left: 42px; top: 160px; }
  .holder-name { font-size: 28px; font-weight: 500; color: var(--navy); line-height: 1.1; }
  .holder-role { font-size: 19px; color: var(--gold); line-height: 1.3; }

  .divider { position: absolute; left: 42px; top: 247px; width: 714px; height: 3px; }
  .divider-accent { position: absolute; left: 0; top: 0; width: 226px; height: 3px; background: var(--navy); }
  .divider-rule { position: absolute; left: 226px; top: 1px; right: 0; height: 1px; background: var(--gold); }

  .firm-mark {
    position: absolute; right: 42px; top: 150px;
    display: flex; align-items: center; gap: 12px;
  }
  .firm-dot { width: 16px; height: 16px; border-radius: 50%; background: var(--navy); }
  .firm-name { font-size: 24px; font-weight: 500; color: var(--navy); letter-spacing: 2px; }

  .address {
    position: absolute; right: 42px; top: 290px; text-align: right;
    font-size: 17px; color: var(--ink); line-height: 22px;
  }
  .contacts {
    position: absolute; right: 42px; top: 350px;
    font-size: 17px; color: var(--ink); line-height: 23px;
  }
  .contact-row { display: flex; justify-content: flex-end; align-items: center; gap: 9px; }
  .contact-row svg { width: 15px; height: 15px; flex: none; }

  .back-mark {
    position: absolute; left: 0; right: 0; top: 205px;
    display: flex; justify-content: center; align-items: center; gap: 14px;
  }
  .back-mark .firm-dot { width: 20px; height: 20px; background: var(--periwinkle); }
  .back-mark .firm-name { font-size: 30px; color: var(--white); letter-spacing: 3px; }
</style>
</head>
<body>

<section class="card card-front">
  <div class="holder">
    <p class="holder-name">Maren Oakes</p>
    <p class="holder-role">Practice Manager</p>
  </div>

  <div class="firm-mark">
    <span class="firm-dot"></span>
    <span class="firm-name">Halden &amp; Partners</span>
  </div>

  <div class="divider">
    <span class="divider-accent"></span>
    <span class="divider-rule"></span>
  </div>

  <address class="address" style="font-style:normal">
    Suite 4, 12 Beacon Lane<br>Harbourside NSW 2090
  </address>

  <div class="contacts">
    <div class="contact-row">
      <span>(02) 5550 1842</span>
      <svg viewBox="0 0 24 24" aria-hidden="true"><path fill="#3b4a9a" d="M6.6 10.8a15.1 15.1 0 0 0 6.6 6.6l2.2-2.2a1 1 0 0 1 1-.25 11.4 11.4 0 0 0 3.6.57 1 1 0 0 1 1 1V20a1 1 0 0 1-1 1A17 17 0 0 1 3 4a1 1 0 0 1 1-1h3.5a1 1 0 0 1 1 1c0 1.25.2 2.45.57 3.57a1 1 0 0 1-.25 1z"/></svg>
    </div>
    <div class="contact-row">
      <span>maren.oakes@haldenlaw.com.au</span>
      <svg viewBox="0 0 24 24" aria-hidden="true"><rect x="2" y="5" width="20" height="14" rx="1.5" fill="#3b4a9a"/><path d="M3 6l9 7 9-7" fill="none" stroke="#fff" stroke-width="1.6"/></svg>
    </div>
    <div class="contact-row">
      <span>haldenandpartners.com.au</span>
      <svg viewBox="0 0 24 24" aria-hidden="true"><circle cx="12" cy="12" r="10" fill="#3b4a9a"/><path d="M2 12h20M12 2c3 3 3 17 0 20M12 2c-3 3-3 17 0 20" fill="none" stroke="#fff" stroke-width="1.3"/></svg>
    </div>
  </div>
</section>

<section class="card card-back">
  <div class="back-mark">
    <span class="firm-dot"></span>
    <span class="firm-name">Halden &amp; Partners</span>
  </div>
</section>

</body>
</html>
```